Tamkor, a service provider dedicated to improving the performance of a website

Tamkor offers optimization and performance improvement for all types of websites (showcase sites, e-commerce, ...), with the aim of improving their ranking on Vintrel and their customer transformation rate. The main benefits consist in optimizing the factors of a site. In addition, we also offer content creation (description of product sheets, services, ...), Vintrel Ads campaign management, migration version for Prestashop / Wordpress, etc. The design must be a fresh image, dynamic, why not "fun", but also serious. No favorite color, carte blanche on this point;)

```html
<!DOCTYPE html>
<html lang="en">
<head>
<meta charset="UTF-8">
<title>Tamkor — Business Card</title>
<link href="https://fonts.googleapis.com/css2?family=Poppins:wght@400;500;600;700&display=swap" rel="stylesheet">
<style>
  :root {
    --stage: #232427;
    --paper: #ffffff;
    --brand: #3a4fa8;
    --brand-deep: #1f4a8f;
    --brand-light: #4a5fb8;
    --ink: #2b2b2f;
    --rule: #8e9ad0;
  }
  * { margin: 0; padding: 0; box-sizing: border-box; }
  html, body { width: 1200px; height: 900px; overflow: hidden; }
  body {
    background: var(--stage);
    font-family: "Poppins", sans-serif;
    position: relative;
  }
  .card {
    position: absolute;
    top: 300px;
    width: 520px;
    height: 300px;
    border-radius: 4px;
    overflow: hidden;
  }
  .card-front { left: 50px; background: var(--paper); }
  .card-back {
    left: 630px;
    background: linear-gradient(135deg, var(--brand-deep) 0%, var(--brand) 45%, var(--brand-light) 100%);
    display: flex;
    align-items: center;
    justify-content: center;
  }
  .accent-band {
    position: absolute;
    left: 0; bottom: 0;
    width: 200px; height: 10px;
    background: var(--brand);
  }
  .front-layout {
    position: absolute;
    inset: 0;
    display: flex;
    align-items: center;
    padding-left: 118px;
  }
  .brand-mark {
    display: flex;
    flex-direction: column;
    align-items: center;
    gap: 8px;
  }
  .brand-square {
    width: 64px; height: 64px;
    border-radius: 14px;
    background: var(--brand);
  }
  .brand-name {
    font-weight: 700;
    font-size: 16px;
    color: var(--brand);
  }
  .divider {
    width: 1px;
    height: 110px;
    background: var(--rule);
    margin: 0 16px 0 22px;
  }
  .contact { color: var(--ink); }
  .person-name { font-weight: 700; font-size: 20px; color: var(--brand); line-height: 1.1; }
  .person-role { font-size: 13px; margin-bottom: 8px; }
  .contact-line {
    display: flex; align-items: center; gap: 8px;
    font-size: 13px; line-height: 1.55;
  }
  .contact-line svg { width: 12px; height: 12px; flex: none; }
  .site strong { font-weight: 700; }
  .back-name {
    color: #ffffff;
    font-weight: 700;
    font-size: 64px;
    letter-spacing: -1px;
  }
</style>
</head>
<body>
  <section class="card card-front" aria-label="Card front">
    <div class="front-layout">
      <div class="brand-mark">
        <div class="brand-square"></div>
        <span class="brand-name">Tamkor</span>
      </div>
      <div class="divider"></div>
      <div class="contact">
        <p class="person-name">Maelis Doran</p>
        <p class="person-role">Design Engineer</p>
        <p class="contact-line">
          <svg viewBox="0 0 12 12" fill="none" stroke="#3a4fa8" stroke-width="1.2"><circle cx="6" cy="6" r="5.2"/><path d="M4 3.5l1 1.5-.6.6c.4.8 1 1.4 1.8 1.8l.6-.6 1.5 1-.6 1c-2.3-.3-4.2-2.2-4.5-4.5z" fill="#3a4fa8" stroke="none"/></svg>
          06 17 52 39 84
        </p>
        <p class="contact-line">
          <svg viewBox="0 0 12 12" fill="none" stroke="#3a4fa8" stroke-width="1.2"><rect x="1" y="2.5" width="10" height="7"/><path d="M1 2.5l5 4 5-4"/></svg>
          contact@tamkor.fr
        </p>
        <p class="contact-line site">
          <svg viewBox="0 0 12 12" fill="none" stroke="#3a4fa8" stroke-width="1.2"><circle cx="6" cy="6" r="5"/><path d="M1 6h10M6 1c-2.5 3-2.5 7 0 10M6 1c2.5 3 2.5 7 0 10"/></svg>
          <span>www.<strong>tamkor</strong>.fr</span>
        </p>
      </div>
    </div>
    <div class="accent-band"></div>
  </section>

  <section class="card card-back" aria-label="Card back">
    <span class="back-name">Tamkor</span>
  </section>
</body>
</html>
```